Wine label for new boutique South African wine focused on the USA market.

Wine label required for new ethical south African red wine called VELMO which stands for 'Pritchard, holloway, mabry and you' but is also a play on 'SA' and that it has a story to tell. Douglas Pritchard is the wine maker, Holloway the farm owner, and Mabry an investor.

Concept is a simple old type writer font on a white/off white label. Front label would say 'Velmo No.1, 2010 Shiraz, South Africa' and similarly a second for another wine 'Velmo No.2, 2010 Cab/Merlot Blend. Maybe the round stain of the bottom of a wine bottle in the bottom corner? Would also like for the 'velmo' to double up as the logo and work in the form of a stamp.

The rear label will need to tell a short story and be able to accommodate the usual boilerplate info. The story will go something like, ' Velmo No.1: It's a long story, but in short we love our wine and we think you will too. The cooling see breezes of the Indian Ocean help define this world class Shiraz from the Western Cape. Aged in french oak for 20 months, the bold flavors will compliment all red meats or simply enjoy on its own. Learn more about our story at www.velmowines-demo.com.

The cab/merlot will read similar: Velmo No.2: It's a long story, but in short we love our wine and we think you will too. The cooling see breezes of the Indian Ocean help define this world class red blend from the Western Cape. Aged in french oak for 20 months, this wine will compliment all red meats or simply enjoy on its own. Learn more about our story at www.velmowines-demo.com.

Reason: Had some great designs already, but as i get to understand how PitchLoom works, I'm keen to explore as many ideas as possible. Neil

Thanks for all the great designs everybody!

We will make a tough decision in the next couple of days.

Regards

Neil

Middle class with some wine knowledge. Price point around $20 -30

Boutique

• A small nod to the wine coming from south Africa in the design would be nice but nothing to over the top
• Simple and clear font with plenty of empty space on the label

```html
<!DOCTYPE html>
<html lang="en">
<head>
<meta charset="utf-8">
<title>Velmo No.2 — Cab/Merlot Blend 2010 Label</title>
<link rel="stylesheet" href="https://fonts.googleapis.com/css2?family=Cinzel:wght@400;700&display=swap">
<style>
  :root {
    --label-black: #141616;
    --accent-yellow: #f5d20f;
    --accent-green: #2b8338;
    --accent-red: #e03a2f;
    --accent-blue: #2b3590;
    --text-white: #ffffff;
  }
  html, body {
    margin: 0;
    padding: 0;
    width: 892px;
    height: 1200px;
    overflow: hidden;
    background: var(--label-black);
  }
  .wine-label {
    display: block;
    width: 892px;
    height: 1200px;
  }
  .label-ground { fill: var(--label-black); }
  .motif-top { fill: url(#motif-top-tone); }
  .motif-bottom { fill: url(#motif-bottom-tone); }
  .motif-left { fill: var(--accent-red); }
  .motif-right { fill: var(--accent-blue); }
  .varietal,
  .origin,
  .brand-name,
  .edition,
  .vintage {
    font-family: 'Cinzel', 'Trajan Pro', serif;
    text-anchor: middle;
  }
  .varietal { fill: var(--text-white); font-size: 46px; font-weight: 400; }
  .origin { fill: var(--text-white); font-size: 19px; font-weight: 700; }
  .brand-name { fill: var(--accent-yellow); font-size: 126px; font-weight: 400; }
  .edition { fill: var(--accent-yellow); font-size: 52px; font-weight: 400; }
  .vintage { fill: var(--accent-yellow); font-size: 48px; font-weight: 400; }
</style>
</head>
<body>
<svg class="wine-label" viewBox="0 0 878 1181" preserveAspectRatio="none" xmlns="http://www.w3.org/2000/svg">
  <defs>
    <linearGradient id="motif-top-tone" x1="0" y1="0" x2="0" y2="1">
      <stop offset="0" stop-color="#2b8338"/>
      <stop offset="1" stop-color="#8fae24"/>
    </linearGradient>
    <linearGradient id="motif-bottom-tone" x1="0" y1="1" x2="0" y2="0">
      <stop offset="0" stop-color="#2b8338"/>
      <stop offset="1" stop-color="#8fae24"/>
    </linearGradient>
  </defs>

  <rect class="label-ground" x="0" y="0" width="878" height="1181"/>

  <polygon class="motif-top" role="img" aria-label="Decorative motif in South African green and yellow" points="118,0 754,0 436,318"/>
  <polygon class="motif-bottom" role="img" aria-label="Decorative motif in South African green and yellow" points="272,1181 600,1181 436,1017"/>
  <rect class="motif-left" role="img" aria-label="Red accent mark" x="0" y="703" width="28" height="94"/>
  <rect class="motif-right" role="img" aria-label="Blue accent mark" x="850" y="703" width="28" height="94"/>

  <text class="varietal" x="440" y="399">Cab/Merlot</text>
  <text class="varietal" x="442" y="442">Blend</text>
  <text class="origin" x="440" y="478">South Africa</text>

  <text class="brand-name" x="446" y="797">VELMO</text>
  <text class="edition" x="444" y="870">No. 2</text>
  <text class="vintage" x="432" y="992">2010</text>
</svg>
</body>
</html>
```